A6 Advertising Post Card

I am looking for refinement on this idea for an advertising letter-box drop of an A6 postcard.
Side 1 - our brand, the address, "15% discount if you present this card before Dec 31"

We are a new retail concept in terms of the store concept.

Side 2 - i want to highlight where the products are from, what materials are used, emphasis on cool, fresh, different, affordable, the product ranges grouped by colours (storage &organisation items in 1 colour or font, illumination products in 1 colour or font, furniture in 1 colour or font, decor in 1 colour or font, curios is 1 colour or font, fasion in 1 colour or font, others in a 1 colour or font)

The Product Categories:
see attachment

Hi

I've added the product categories with products sorted under each heading. I have also added the logo in a variety of file types (jpg, tif, psd, png). The sky blue background is part of the brand image.
Thanks

Target Market(s)

Home-makers (men and women) and women of all ages. Decision makers for home furnishings. Cross demographic - this is not premium..affordable to all social strata.
The brand is about fun, colourful and functional home stuff. The fashion stuff is a small percentage of the overall offer - targeting women who should spoil themselves as they spoil their families with nice stuff for the home.

Industry/Entity Type

Advertising

```html
<!DOCTYPE html>
<html lang="en">
<head>
<meta charset="utf-8">
<title>Kelora – A6 Postcard</title>
<link rel="stylesheet" href="https://fonts.googleapis.com/css2?family=Quicksand:wght@500;700&family=PT+Sans+Narrow:wght@400;700&display=swap">
<style>
  :root {
    --stage: #ebebeb;
    --brand-sky: #68c5cc;
    --band: #a8a6ba;
    --ink: #2c2a4e;
    --logo-blue: #2d5aa6;
    --diamond: #6b7391;
    --sticker: #3d3f66;
    --sticker-light: #5a5c86;
    --white: #ffffff;
  }
  html, body {
    margin: 0;
    padding: 0;
    width: 1200px;
    height: 1000px;
    overflow: hidden;
    background: var(--stage);
  }
  .postcard {
    position: absolute;
    left: 100px;
    top: 145px;
    width: 700px;
    height: 497px;
    transform: scale(1.4286);
    transform-origin: top left;
    background: var(--brand-sky);
    overflow: hidden;
    box-shadow: 0 1px 3px rgba(0,0,0,0.18);
  }
  .brand-name {
    position: absolute;
    left: 0;
    right: 0;
    top: 58px;
    margin: 0;
    text-align: center;
    font-family: "Quicksand", sans-serif;
    font-weight: 700;
    font-size: 100px;
    line-height: 1.2;
    color: var(--logo-blue);
    letter-spacing: 1px;
  }
  .tagline {
    position: absolute;
    left: 0;
    right: 0;
    top: 244px;
    margin: 0;
    text-align: center;
    font-family: "Quicksand", sans-serif;
    font-weight: 500;
    font-size: 27px;
    color: var(--ink);
    padding-left: 40px;
  }
  .tagline .divider {
    display: inline-block;
    width: 10px;
    height: 10px;
    margin: 0 10px 5px;
    background: var(--diamond);
    transform: rotate(45deg);
    vertical-align: middle;
  }
  .address-band {
    position: absolute;
    left: 0;
    right: 0;
    bottom: 0;
    height: 60px;
    background: var(--band);
  }
  .address {
    position: absolute;
    right: 34px;
    top: 12px;
    margin: 0;
    text-align: right;
    font-family: "PT Sans Narrow", sans-serif;
    font-weight: 400;
    font-size: 11.5px;
    line-height: 16px;
    font-style: normal;
    color: var(--ink);
  }
  .discount-sticker {
    position: absolute;
    left: 20px;
    top: 257px;
    width: 240px;
    height: 240px;
  }
  .discount-sticker svg {
    position: absolute;
    inset: 0;
    overflow: visible;
  }
  .sticker-copy {
    position: absolute;
    left: 46px;
    top: 52px;
    width: 160px;
    transform: rotate(-17deg);
    transform-origin: center;
    font-family: "PT Sans Narrow", sans-serif;
    color: var(--white);
    text-align: center;
  }
  .sticker-copy .amount {
    display: block;
    font-weight: 700;
    font-size: 62px;
    line-height: 56px;
    margin-left: -18px;
  }
  .sticker-copy .label {
    display: block;
    font-weight: 700;
    font-size: 31px;
    line-height: 30px;
    margin-left: 14px;
  }
  .sticker-copy .terms {
    display: block;
    font-weight: 400;
    font-size: 11px;
    line-height: 13px;
    margin: 4px 0 0 22px;
  }
</style>
</head>
<body>
  <main class="postcard">
    <h1 class="brand-name">Kelora</h1>
    <p class="tagline">home<span class="divider"></span>gifts</p>

    <footer class="address-band">
      <address class="address">42 Linden Row &nbsp;|&nbsp; 42 Linden Row Eastvale SA 5999<br>www.kelora.com.au</address>
    </footer>

    <div class="discount-sticker">
      <svg viewBox="0 0 240 240" width="240" height="240" aria-hidden="true">
        <defs>
          <clipPath id="sticker-unpeeled">
            <polygon points="-20,-20 260,-20 260,132 236,150 116,240 -20,260"/>
          </clipPath>
          <radialGradient id="sticker-face" cx="0.35" cy="0.35" r="0.75">
            <stop offset="0" stop-color="var(--sticker-light)"/>
            <stop offset="1" stop-color="var(--sticker)"/>
          </radialGradient>
          <linearGradient id="peel-flap" x1="0" y1="0" x2="1" y2="1">
            <stop offset="0" stop-color="#ffffff"/>
            <stop offset="0.55" stop-color="#e4e4ea"/>
            <stop offset="1" stop-color="#9c9cab"/>
          </linearGradient>
        </defs>
        <g clip-path="url(#sticker-unpeeled)">
          <circle cx="120" cy="120" r="119" fill="var(--white)"/>
          <circle cx="120" cy="120" r="111" fill="url(#sticker-face)"/>
          <circle cx="120" cy="120" r="101" fill="none" stroke="var(--white)" stroke-width="2"/>
        </g>
        <path d="M236,150 C214,160 186,170 168,182 C150,194 140,210 116,240 C150,224 176,206 198,188 C214,174 228,162 236,150 Z"
              fill="url(#peel-flap)" stroke="#c9c9d3" stroke-width="0.6"/>
      </svg>
      <p class="sticker-copy">
        <span class="amount">15%</span>
        <span class="label">DISCOUNT</span>
        <span class="terms">*15% discount if you present this card before Dec 31 2013</span>
      </p>
    </div>
  </main>
</body>
</html>
```